Dentistry Office

We want a new design for a Dentist's office website.

The theme is: "We provide high quality, state-of-the-art, dental care in a comfortable, caring environment."

The site currently has a menu on the left of the page with about 40 items on it. There is a great deal of textual content on each page, plus several illustrations.

We want to do this using CSS, so we need specifications in the CSS for all possible elements. The CSS needs to be named in a logical manner for easy use.

Every dentist on the planet seems to use lots of Flash. We don't want to because it is so distracting. We are looking for an elegant solution targeting 24-55 age group, but not excluding anyone.

The following (from another dentist's site) can give you a taste of what we want to communicate on the site:

"After 20 years of teaching dentists how to refine their technique and many years of writing textbooks, I currently devote my time to my office and the hands-on practice of dentistry. I'd like to welcome you personally to my dental practice, and I invite you to meet my highly experienced team of professionals.

"We have offered complete dental care of the highest quality since 1978. We provide Preventive Services, Tooth Whitening and Cosmetic Dentistry for a beautiful smile, Endodontics (root canal treatment) to treat painful teeth, Sedation Dentistry so you can relax, and Dental Implants to restore what is missing. We offer total care.

"Our approach to your health is simple: We use our education, experience and dedication to provide every patient with superior dental care.

"This passion for excellence is not just a goal, but a standard every member of our team holds.

"We also pride ourselves with our state of the art procedures, training and technology. This includes creating a beautiful smile using techniques that preserve as much of the original tooth as possible.

"Our abilities are renowned throughout the dental profession and I hope if you have any questions you will contact us by an e-mail note, by phone or just by dropping by."

Keep in mind the screen shape and dimensions. Your design needs to work in the normal screen proportions, regardless of how it looks when you post it here. Scrolling is OK, but the first impression needs to work.

Keep in mind that there will be about 250 words, or more, on each page.

Competitors web sites:

http://www.brevalkoortho.example/

http://www.quimbelfieldcare.example/

http://www.grinsatdoverellclinic.example/

http://www.trunwickfamilydentalcare.example/

http://www.morvanhaledental.example/

http://www.ubrigandental.example/

We need to compete with these.

Target Market(s)

Generally adults seeking the most experienced and comfortable-to-be-with dentist.

Industry/Entity Type

Training

Requirements
Must have
• Must stand apart from other dentists.
• Must be elegant.
• Must have a horizontal menu structure across all columns, NOT a vertical that requires scrolling, no popout, pop down, etc. menus.
• We are looking for something special.
• Do not waste your time or ours putting up templates and things you have used before.
• Personally, I do not see how someone outside the US can understand the northern California dental market. But you are welcome to try.
Should not have
• Flash or graphics that move
• The look of a template
• Folksy fonts
• Looks like you used it 20 times before

```html
<!DOCTYPE html>
<html lang="en">
<head>
<meta charset="utf-8">
<title>Larkmoor Dentist</title>
<link href="https://fonts.googleapis.com/css2?family=Noto+Sans:wght@400;700&family=Arimo:wght@400;700&display=swap" rel="stylesheet">
<style>
:root{
  --header-top:#8c9aae;
  --header-bottom:#4f5b6c;
  --nav:#67717f;
  --nav-text:#ffffff;
  --page:#f6f6f6;
  --side-panel:#e6e7e8;
  --side-head:#6a7381;
  --text:#3a3a3a;
  --heading:#4d5866;
  --tick:#5e9ea6;
  --promo:#dcdacb;
  --promo-band:#8f8f80;
  --footer:#6a7382;
  --link-teal:#5b8f98;
}
*{margin:0;padding:0;box-sizing:border-box}
html,body{width:936px;height:1200px;overflow:hidden;background:var(--page)}
body{position:relative;font-family:"Arimo",Arial,sans-serif;color:var(--text)}
.abs{position:absolute}

.site-header{left:0;top:0;width:936px;height:244px;background:linear-gradient(180deg,var(--header-top),var(--header-bottom))}
.header-photo{left:470px;top:0;width:440px;height:244px;background:linear-gradient(90deg,rgba(140,154,174,0),rgba(205,200,196,.55) 45%,rgba(120,132,150,.3))}
.site-title{left:82px;top:68px;font-family:"Noto Sans",sans-serif;font-weight:400;font-size:32px;line-height:38px;color:#e9ecf0;text-shadow:0 1px 2px rgba(0,0,0,.35);white-space:nowrap}
.appointments{left:83px;top:192px;font-family:"Noto Sans",sans-serif;font-size:15px;letter-spacing:.3px;color:#fff;white-space:nowrap}

.main-nav{left:0;top:244px;width:936px;height:38px;background:var(--nav)}
.nav-item{top:0;height:38px;line-height:38px;font-family:"Noto Sans",sans-serif;font-size:11.5px;font-weight:700;color:var(--nav-text);letter-spacing:.4px;white-space:nowrap}
.nav-item.active{background:var(--page);color:#3e4b5c;padding:0 14px;left:77px;width:64px;line-height:40px}
.nav-sep{top:10px;width:1px;height:20px;background:#c8ccd2}

.topic-panel{left:77px;top:305px;width:184px;height:274px;background:var(--side-panel)}
.topic-head{left:77px;width:184px;height:25px;background:var(--side-head);color:#fff;font-size:12px;font-weight:700;letter-spacing:.8px;line-height:25px;padding-left:12px;border-bottom:1px solid #aab;white-space:nowrap}
.topic-link{left:87px;font-size:10.6px;letter-spacing:.3px;color:#444;white-space:nowrap}
.topic-link::before{content:"";display:inline-block;width:0;height:0;border-left:4px solid #555;border-top:3.5px solid transparent;border-bottom:3.5px solid transparent;margin-right:8px;vertical-align:1px}

.section-title{font-family:"Noto Sans",sans-serif;font-weight:400;font-size:16px;color:var(--heading);letter-spacing:.4px;white-space:nowrap}
.welcome-text{left:288px;top:323px;font-size:10.6px;line-height:15.3px;letter-spacing:.15px;white-space:nowrap}
.office-photo{left:672px;top:313px;width:185px;height:140px;border:2px solid #dde0e3;background:linear-gradient(160deg,#6f8a5a,#8a6f5a 45%,#7a8a6a 70%,#b6bac0)}

.services{left:286px;top:481px;width:600px;list-style:none}
.services li{position:relative;height:18.7px;font-size:10.4px;line-height:14px;letter-spacing:.4px;padding-left:20px;white-space:nowrap}
.services svg{position:absolute;left:0;top:1px}

.promo{left:295px;top:678px;width:532px;height:156px;border:1px solid #c9c7b5;border-radius:4px;background:var(--promo);overflow:hidden}
.promo-photo{position:absolute;left:343px;top:0;width:189px;height:156px;background:linear-gradient(135deg,#c9b69c,#e6d2b8 50%,#a78d73)}
.promo-band{position:absolute;left:0;top:119px;width:380px;height:37px;background:linear-gradient(90deg,var(--promo-band),rgba(143,143,128,.5))}
.promo-title{position:absolute;left:12px;top:16px;font-size:17px;line-height:31px;color:#3c3c30;letter-spacing:1.2px;white-space:nowrap}
.promo-link{position:absolute;left:255px;top:88px;font-family:"Noto Sans",sans-serif;font-size:10.5px;color:#333;letter-spacing:.4px}
.promo-note{position:absolute;left:7px;top:122px;font-size:9.6px;line-height:15px;color:#fff;letter-spacing:.5px;white-space:nowrap}

.info-btn{left:300px;width:215px;height:34px;border-radius:4px 4px 0 0;background:linear-gradient(100deg,#6c7583 70%,#9aa1ab 71%);color:#fff;font-size:15px;line-height:34px;padding-left:17px;letter-spacing:.5px}
.info-btn.rounded{border-radius:4px}
.call-box{left:300px;top:1044px;width:215px;height:54px;background:#e4e4e2;font-size:9.8px;line-height:15.3px;padding:4px 6px;letter-spacing:.7px;color:#333;border-radius:0 0 4px 4px}

.map-box{left:570px;top:871px;width:258px;height:233px;border:2px solid #c9c9c6;background:linear-gradient(160deg,#e1e0dc,#d6d5d0)}

.site-footer{left:0;top:1126px;width:936px;height:74px;background:var(--footer)}
.footer-links{left:92px;top:1136px;font-family:"Noto Sans",sans-serif;font-size:10.2px;color:#fff;white-space:nowrap}
.copyright{left:92px;top:1162px;font-family:"Noto Sans",sans-serif;font-size:10.2px;color:#fff}
.top-tab{left:774px;top:1126px;width:53px;height:27px;background:var(--page);color:var(--link-teal);font-size:12px;text-align:center;line-height:28px}
</style>
</head>
<body>

<header class="abs site-header">
  <div class="abs header-photo" role="img" aria-label="Photo of a smiling woman raising her arms"></div>
  <h1 class="abs site-title">Larkmoor Dentist<br>Corwin Halvey, DDS, FAGD</h1>
  <p class="abs appointments">For Appointments: (555) 014-2290.</p>
</header>

<nav class="abs main-nav">
  <span class="abs nav-item active">Home</span>
  <span class="abs nav-item" style="left:157px">Why we are differnt</span>
  <span class="abs nav-sep" style="left:296px"></span>
  <span class="abs nav-item" style="left:314px">Technologies we offer</span>
  <span class="abs nav-sep" style="left:469px"></span>
  <span class="abs nav-item" style="left:486px">Meet Dr.Halvey</span>
  <span class="abs nav-sep" style="left:592px"></span>
  <span class="abs nav-item" style="left:609px">Our Staff</span>
  <span class="abs nav-sep" style="left:686px"></span>
  <span class="abs nav-item" style="left:701px">Contact Us</span>
  <span class="abs nav-sep" style="left:789px"></span>
  <span class="abs nav-item" style="left:808px">Links</span>
</nav>

<aside aria-label="Dental health topics">
  <div class="abs topic-panel"></div>
  <h3 class="abs topic-head" style="top:305px">EDUCATION</h3>
  <span class="abs topic-link" style="top:342px">Emergency Dental Care</span>
  <span class="abs topic-link" style="top:368px">Your Mouth</span>
  <span class="abs topic-link" style="top:393px">Your Tooth</span>
  <span class="abs topic-link" style="top:419px">Cracked Tooth?</span>
  <span class="abs topic-link" style="top:444px">Missing a Tooth?</span>
  <span class="abs topic-link" style="top:470px">Sensitive Teeth</span>
  <span class="abs topic-link" style="top:495px">Dry MouthTooth</span>
  <span class="abs topic-link" style="top:521px">GrindingSleep</span>
  <span class="abs topic-link" style="top:546px">Dentistry</span>
  <h3 class="abs topic-head" style="top:580px">PREVENTATIVE</h3>
  <h3 class="abs topic-head" style="top:606px">COSMETICS</h3>
  <h3 class="abs topic-head" style="top:631px">RESTORATIONS</h3>
  <h3 class="abs topic-head" style="top:657px;padding-left:9px">VISITING OUR OFFICE</h3>
</aside>

<main>
  <h2 class="abs section-title" style="left:289px;top:301px">Welcome</h2>
  <p class="abs welcome-text">Lorem ipsum dolor sit amet, consectetuer adipiscing elit. Aenean commodo<br>ligula eget dolor. Aenean massa. Cum sociis natoque penatibus et magnis<br>dis parturient montes, nascetur ridiculus mus. Doneuam felis, ultricies nec,<br>pellentesque eu, pretium quis, sem. Nulla consequat massa quis enim.<br>Donec pede justo, fringilla vel, aliquet nec, vulputate eget, arcu. In enim<br>justo, rhoncus ut, imperdiet a, venenatis vitae, justo.massa quis enim.<br>Donec pede justo,</p>
  <div class="abs office-photo" role="img" aria-label="Photo of the dental office building with garden"></div>

  <h2 class="abs section-title" style="left:289px;top:450px">Dr. Halvey Provides</h2>
  <ul class="abs services">
    <li><svg width="11" height="10" viewBox="0 0 11 10"><path d="M1 5l3 3 6-7" fill="none" stroke="#5e9ea6" stroke-width="2"/></svg>General dentistry—oral hygiene, cavity detection and repair, crowns.</li>
    <li><svg width="11" height="10" viewBox="0 0 11 10"><path d="M1 5l3 3 6-7" fill="none" stroke="#5e9ea6" stroke-width="2"/></svg>Cosmetic/restorative dentistry—broken or misshapen teeth, crooked smiles, unsightly gaps</li>
    <li><svg width="11" height="10" viewBox="0 0 11 10"><path d="M1 5l3 3 6-7" fill="none" stroke="#5e9ea6" stroke-width="2"/></svg>Non-metal fillings—nontoxic, durable tooth-colored resin fillings that are proven to provide better results</li>
    <li><svg width="11" height="10" viewBox="0 0 11 10"><path d="M1 5l3 3 6-7" fill="none" stroke="#5e9ea6" stroke-width="2"/></svg>Tooth shaping—extending, shortening or otherwise reshaping teeth for improved esthetics</li>
    <li><svg width="11" height="10" viewBox="0 0 11 10"><path d="M1 5l3 3 6-7" fill="none" stroke="#5e9ea6" stroke-width="2"/></svg>Complete smile make-over's—resin veneers that reshape the whole mouth while preserving natural teeth</li>
    <li><svg width="11" height="10" viewBox="0 0 11 10"><path d="M1 5l3 3 6-7" fill="none" stroke="#5e9ea6" stroke-width="2"/></svg>Tooth whitening—at-home bleaching options to make teeth appear years younger</li>
    <li><svg width="11" height="10" viewBox="0 0 11 10"><path d="M1 5l3 3 6-7" fill="none" stroke="#5e9ea6" stroke-width="2"/></svg>Laser Dentistry, Sleep Dentistry, and Implant Dentistry with the Finest and Latest Equipment and Materials.</li>
    <li><svg width="11" height="10" viewBox="0 0 11 10"><path d="M1 5l3 3 6-7" fill="none" stroke="#5e9ea6" stroke-width="2"/></svg>Dental Implants to replace missing teeth.</li>
    <li><svg width="11" height="10" viewBox="0 0 11 10"><path d="M1 5l3 3 6-7" fill="none" stroke="#5e9ea6" stroke-width="2"/></svg>Sedation Dentistry so you can be relaxed.</li>
  </ul>

  <section class="abs promo">
    <div class="promo-photo" role="img" aria-label="Photo of a laughing young couple"></div>
    <div class="promo-band"></div>
    <p class="promo-title">We offer an Initial Patient Examination<br>X-rays and Cleaning for $79.00.</p>
    <span class="promo-link">Learn More</span>
    <p class="promo-note">New patients only. Offers are cash patients only.<br>Insurance will be billed at full value.</p>
  </section>

  <div class="abs info-btn rounded" style="top:872px">Office Hours</div>
  <svg class="abs" style="left:471px;top:860px" width="36" height="36" viewBox="0 0 36 36"><circle cx="18" cy="18" r="16" fill="#f3a81c"/><circle cx="18" cy="18" r="12" fill="#fff"/><path d="M18 9v9l6 3" fill="none" stroke="#555" stroke-width="2"/></svg>
  <div class="abs info-btn rounded" style="top:940px">Where to stay?</div>
  <svg class="abs" style="left:471px;top:928px" width="36" height="36" viewBox="0 0 36 36"><circle cx="18" cy="18" r="16" fill="#e8eef5" stroke="#c9d3de"/><circle cx="18" cy="18" r="13" fill="#2f7fd6"/><text x="18" y="24" font-family="Arial,sans-serif" font-size="17" font-weight="700" fill="#fff" text-anchor="middle">?</text></svg>
  <div class="abs info-btn" style="top:1010px">please call</div>
  <svg class="abs" style="left:462px;top:988px" width="42" height="44" viewBox="0 0 42 44"><path d="M32 4c4 2 6 4 4 8l-4 4c-2 1-3 0-4-1-4 6-8 14-9 20 2 0 3 1 3 3l-1 5c-1 3-5 2-8 0C10 32 22 10 32 4z" fill="#d63a2a"/></svg>
  <p class="abs call-box">contact us outside office hours for an emergency, please call at<br>(555) 013-7741.</p>

  <h2 class="abs section-title" style="left:574px;top:845px">Map to Office</h2>
  <div class="abs map-box" role="img" aria-label="Street map showing directions to the office"></div>
</main>

<footer>
  <div class="abs site-footer"></div>
  <p class="abs footer-links">Larkmoor Dentist • Tell A Friend • Privacy &amp; Legal • Dental Resources • New Patient Forms</p>
  <p class="abs copyright">Copyright © 2009. All Rights Reserved</p>
  <span class="abs top-tab">Top</span>
</footer>

</body>
</html>
```